KVRo Business Cards

We need a business card design. We are a Technology (Audio Visual) design, sales and installation company. Looking for a double sided design, clean

Contact Information for Business Card

Clean, modern look, 2 sided

Font styles to use
Sans Serif

```html
<!DOCTYPE html>
<html lang="en">
<head>
<meta charset="utf-8">
<title>KVRo Business Cards</title>
<link rel="stylesheet" href="https://fonts.googleapis.com/css2?family=Montserrat:wght@800&family=Open+Sans:wght@400;600&display=swap">
<style>
  :root {
    --navy: #1c2f42;
    --navy-deep: #172838;
    --orange: #f7941d;
    --white: #ffffff;
    --ink: #3d4650;
    --stage: #e9ebee;
  }
  * { margin: 0; padding: 0; box-sizing: border-box; }
  html, body { width: 1200px; height: 900px; overflow: hidden; }
  body {
    background: var(--stage);
    font-family: "Open Sans", Arial, sans-serif;
    position: relative;
  }
  .card {
    position: absolute;
    left: 320px;
    width: 560px;
    height: 320px;
    overflow: hidden;
    box-shadow: 0 6px 18px rgba(0,0,0,0.18);
  }
  .card-back { top: 70px; background: var(--navy-deep); }
  .card-front { top: 470px; background: var(--white); }

  .back-name {
    position: absolute;
    right: 70px;
    top: 120px;
    font-family: "Montserrat", Arial, sans-serif;
    font-weight: 800;
    font-size: 44px;
    color: var(--white);
    letter-spacing: 1px;
  }

  .front-name {
    position: absolute;
    left: 34px;
    top: 92px;
    font-family: "Montserrat", Arial, sans-serif;
    font-weight: 800;
    font-size: 76px;
    line-height: 1;
    color: var(--navy);
  }
  .divider {
    position: absolute;
    left: 262px;
    top: 92px;
    width: 2px;
    height: 132px;
    background: var(--navy);
  }
  .contact {
    position: absolute;
    left: 282px;
    top: 90px;
    color: var(--ink);
    font-size: 14.5px;
    line-height: 1.25;
  }
  .person-name {
    font-family: "Montserrat", Arial, sans-serif;
    font-weight: 800;
    font-size: 19px;
    color: var(--navy);
    letter-spacing: 0.5px;
  }
  .person-role { font-size: 14.5px; margin-bottom: 12px; }
  .address { margin-bottom: 8px; }
  .line { display: flex; align-items: center; gap: 6px; }
  .line svg { width: 12px; height: 12px; flex: none; }
  .wave { position: absolute; left: 0; top: 0; width: 560px; height: 320px; }
  .website {
    position: absolute;
    right: 36px;
    bottom: 18px;
    color: var(--white);
    font-size: 16px;
    letter-spacing: 0.5px;
  }
</style>
</head>
<body>
  <section class="card card-back" aria-label="Card back">
    <div class="back-name">KVRo</div>
  </section>

  <section class="card card-front" aria-label="Card front">
    <svg class="wave" viewBox="0 0 560 320" aria-hidden="true">
      <path d="M0 200 Q130 262 300 262 Q450 262 560 250 L560 320 L0 320 Z" fill="var(--navy)"/>
      <path d="M0 184 Q110 232 290 248 Q140 246 0 196 Z" fill="var(--orange)"/>
      <path d="M300 250 Q440 248 560 226 L560 238 Q440 258 300 250 Z" fill="var(--orange)"/>
    </svg>

    <div class="front-name">KVRo</div>
    <div class="divider"></div>

    <div class="contact">
      <div class="person-name">EVAN MARLOWE</div>
      <div class="person-role">President</div>
      <div class="address">1870 Harbor Crest Way<br>Seacliff CA 90412</div>
      <div class="line">
        <svg viewBox="0 0 24 24"><path fill="var(--orange)" d="M6.6 10.8a15.1 15.1 0 0 0 6.6 6.6l2.2-2.2a1 1 0 0 1 1-.25 11.4 11.4 0 0 0 3.6.57 1 1 0 0 1 1 1V20a1 1 0 0 1-1 1A17 17 0 0 1 3 4a1 1 0 0 1 1-1h3.5a1 1 0 0 1 1 1c0 1.25.2 2.45.57 3.57a1 1 0 0 1-.25 1z"/></svg>
        <span>555-310-4827</span>
      </div>
      <div class="line">
        <svg viewBox="0 0 24 24"><path fill="var(--orange)" d="M2 5h20v14H2z M2 5l10 8 10-8" stroke="var(--white)" stroke-width="1.5"/></svg>
        <span>evanmarlowe@kvro.com</span>
      </div>
    </div>

    <div class="website">www.kvro.com</div>
  </section>
</body>
</html>
```